I need the following on my business card:
- Name: Dana Whitcomb
- License # 0M93216
- Title: Producer
- Phone: (555) 017-3904
- Email: Dana@CorbelInsuranceServices.com

- Company: Corbel Insurance Services
- Address: 27408 Larkmoor Ave Suite 610, Fenwick Grove, CA 90217
- Website: www.CorbelInsuranceServices.com

Also add our slogan on the card: "Where Care Finds Coverage"

```html
<!DOCTYPE html>
<html lang="en">
<head>
<meta charset="utf-8">
<title>Corbel Insurance Services – Business Card</title>
<link href="https://fonts.googleapis.com/css2?family=Figtree:wght@400;500;700;800&display=swap" rel="stylesheet">
<style>
  :root {
    --navy: #27306f;
    --green: #0c9b48;
    --ink: #1a1a1a;
    --paper: #ffffff;
    --backdrop: #e3e7e5;
  }
  * { box-sizing: border-box; margin: 0; padding: 0; }
  html, body {
    width: 1200px; height: 716px; overflow: hidden;
    background: var(--backdrop);
    font-family: "Figtree", "Helvetica Neue", Arial, sans-serif;
  }
  .card {
    position: absolute;
    left: 370px;
    width: 460px;
    height: 264px;
    background: var(--paper);
    border-radius: 12px;
    overflow: hidden;
    box-shadow: 0 2px 8px rgba(0,0,0,0.18);
  }
  .card--front { top: 94px; }
  .card--back { top: 382px; }

  .brand-name {
    color: var(--navy);
    font-weight: 800;
    white-space: nowrap;
  }
  .brand-mark {
    border-radius: 50%;
    background: var(--green);
    flex: none;
  }
  .card--front .brand {
    position: absolute;
    left: 0; right: 0; top: 112px;
    display: flex; justify-content: center; align-items: center; gap: 9px;
  }
  .card--front .brand-name { font-size: 23px; }
  .card--front .brand-mark { width: 16px; height: 16px; }

  .card--back .brand {
    position: absolute; left: 24px; top: 45px;
    display: flex; align-items: center; gap: 7px;
  }
  .card--back .brand-name { font-size: 13.5px; }
  .card--back .brand-mark { width: 11px; height: 11px; }

  .person-name {
    position: absolute; right: 16px; top: 102px;
    font-size: 16px; font-weight: 800; color: var(--navy);
  }
  .divider {
    position: absolute; left: 17px; top: 133px;
    width: 374px; height: 1.5px; background: var(--navy);
  }
  .person-title {
    position: absolute; right: 16px; top: 125px;
    font-size: 11.5px; font-weight: 500; color: var(--ink);
  }

  .details {
    position: absolute; top: 164px;
    font-size: 12.5px; line-height: 16.5px; color: var(--ink);
  }
  .details--address { left: 18px; }
  .details--contact { right: 16px; text-align: right; }
  .contact-line {
    display: flex; justify-content: flex-end; align-items: center; gap: 5px;
  }
  .contact-line svg { width: 10px; height: 10px; fill: var(--navy); flex: none; }

  .footer {
    position: absolute; left: 0; bottom: 0; width: 460px; height: 40px;
  }
  .slogan {
    position: absolute; left: 0; right: 0; bottom: 10px;
    text-align: center; color: #fff;
    font-size: 12.5px; font-weight: 500;
  }
</style>
</head>
<body>

<section class="card card--front">
  <div class="brand">
    <span class="brand-mark"></span>
    <span class="brand-name">Corbel Insurance Services</span>
  </div>
</section>

<section class="card card--back">
  <div class="brand">
    <span class="brand-mark"></span>
    <span class="brand-name">Corbel Insurance Services</span>
  </div>

  <div class="person-name">Dana Whitcomb</div>
  <div class="divider"></div>
  <div class="person-title">Producer</div>

  <div class="details details--address">
    <p>License # 0M93216</p>
    <p>27408 Larkmoor Ave Suite 610,</p>
    <p>Fenwick Grove, CA 90217</p>
  </div>

  <div class="details details--contact">
    <p class="contact-line">(555) 017-3904
      <svg viewBox="0 0 10 10" aria-hidden="true"><path d="M1 4.2C1 2.6 3 2 5 2s4 .6 4 2.2v.8H7.2V4H2.8v1H1z"/><path d="M2.3 5.4 3.4 4.5h3.2l1.1.9V8.5H2.3z"/></svg>
    </p>
    <p class="contact-line">Dana@CorbelInsuranceServices.com
      <svg viewBox="0 0 10 10" aria-hidden="true"><path d="M0.5 2h9v0.8L5 5.8 0.5 2.8z"/><path d="M0.5 3.8 5 6.8l4.5-3V8h-9z"/></svg>
    </p>
    <p class="contact-line">www.CorbelInsuranceServices.com
      <svg viewBox="0 0 10 10" aria-hidden="true"><circle cx="5" cy="5" r="4.5"/><path d="M3 2.5c1 .3 1.5 1 1 1.8S2.5 5 2.8 6 4 6.8 4 8M6.5 2c-.3 1 .3 1.5 1.2 1.6M6 6c1 0 1.5.8 1.2 1.8" stroke="#fff" stroke-width=".7" fill="none"/></svg>
    </p>
  </div>

  <svg class="footer" viewBox="0 0 460 40" aria-hidden="true">
    <rect x="0" y="26" width="460" height="14" fill="var(--navy)"/>
    <path d="M105 40 C118 14 126 3 160 3 H300 C334 3 342 14 355 40 Z" fill="#fff"/>
    <path d="M109 40 C121 16 129 6 162 6 H298 C331 6 339 16 351 40 Z" fill="var(--green)"/>
  </svg>
  <p class="slogan">Where Care Finds Coverage</p>
</section>

</body>
</html>
```